Unique business card design

Boutique coastal hotel suites - in need of clever stand out business card I have uploaded the logo that I had created through quill forge I want something that is clever and stands out from everyone else - 418 Brantwell Avenue kestrelport Alaska 99571 phone or text 907 -581-6142 www.primemarrowbysuites.com

Target Market(s)

Men and woman

Industry/Entity Type

Boutique coastal hotel

Contact Information for Business Card

Marrowby Suites Seldovia Alaska marrowby_suites@mailnest.net

Requirements
Must have
• Classy - clever -bold 907-581-6142 call or text

```html
<!DOCTYPE html>
<html lang="en">
<head>
<meta charset="utf-8">
<title>Marrowby Suites – Business Card</title>
<link rel="stylesheet" href="https://fonts.googleapis.com/css2?family=Poppins:wght@400;500&display=swap">
<style>
  :root {
    --stage: #0b0b0b;
    --card-black: #0f0f0f;
    --pattern-tone: #1a1a1a;
    --gold: #d9c43a;
    --gold-deep: #b89a12;
    --paper: #e9e7e1;
    --ink-white: #f1f1f1;
    --navy: #1d2f55;
  }
  html, body {
    margin: 0;
    width: 1200px;
    height: 750px;
    overflow: hidden;
    background: var(--stage);
  }
  .stage {
    position: relative;
    width: 1200px;
    height: 750px;
  }
  .card {
    position: absolute;
    top: 214px;
    width: 520px;
    height: 322px;
    box-shadow: 0 22px 40px rgba(0,0,0,0.6);
  }
  .card--front { left: 50px; }
  .card--back { left: 630px; }
  .card svg { display: block; width: 520px; height: 322px; }
  .brand-name {
    font-family: "Poppins", sans-serif;
    font-weight: 500;
    fill: var(--gold);
  }
  .contact-text {
    font-family: "Poppins", sans-serif;
    font-weight: 400;
    font-size: 11px;
    fill: var(--ink-white);
  }
  .web-address {
    font-family: "Poppins", sans-serif;
    font-weight: 400;
    font-size: 12.5px;
    fill: var(--gold);
  }
  .mini-name {
    font-family: "Poppins", sans-serif;
    font-weight: 500;
    font-size: 9px;
    fill: var(--navy);
    letter-spacing: 1px;
  }
</style>
</head>
<body>
<main class="stage">

  <!-- Front of card -->
  <section class="card card--front">
    <svg viewBox="0 0 520 322" xmlns="http://www.w3.org/2000/svg">
      <rect class="card-base" width="520" height="322" fill="var(--card-black)"/>
      <rect class="damask-area" role="img" aria-label="subtle dark damask pattern across the card face" width="520" height="322" fill="var(--pattern-tone)"/>

      <line class="rule rule--top" x1="93" y1="125" x2="428" y2="125" stroke="var(--gold)" stroke-width="1.2"/>
      <text class="brand-name" x="92" y="168" font-size="42" letter-spacing="5">MARROWBY</text>
      <line class="rule rule--bottom" x1="92" y1="189" x2="256" y2="189" stroke="var(--gold)" stroke-width="1.2"/>
      <text class="brand-name" x="266" y="193" font-size="11" letter-spacing="15">SUITES</text>

      <text class="web-address" x="357" y="272" text-anchor="end">www.primemarrowbysuites.com</text>
      <rect class="gold-bar" x="8" y="289" width="506" height="6" fill="var(--gold)"/>
    </svg>
  </section>

  <!-- Back of card -->
  <section class="card card--back">
    <svg viewBox="0 0 520 322" xmlns="http://www.w3.org/2000/svg">
      <defs>
        <linearGradient id="goldSheen" x1="0" y1="0" x2="1" y2="1">
          <stop offset="0" stop-color="var(--gold-deep)"/>
          <stop offset="0.5" stop-color="var(--gold)"/>
          <stop offset="1" stop-color="var(--gold-deep)"/>
        </linearGradient>
      </defs>
      <rect class="card-base" width="520" height="322" fill="var(--card-black)"/>
      <polygon class="damask-area" role="img" aria-label="subtle dark damask pattern on the left panel" points="0,0 110,0 191,159 262,300 270,322 0,322" fill="var(--pattern-tone)"/>
      <polygon class="paper-triangle" points="110,0 285,0 191,159" fill="var(--paper)"/>
      <polygon class="gold-slant" points="247,276 381,276 355,322 270,322" fill="url(#goldSheen)"/>
      <polygon class="paper-strip" points="405,274 520,271 520,322 362,322" fill="var(--paper)"/>

      <text class="brand-name" x="297" y="90" font-size="29" letter-spacing="3">MARROWBY</text>
      <line class="rule" x1="290" y1="100" x2="382" y2="100" stroke="var(--gold)" stroke-width="1"/>
      <text class="brand-name" x="390" y="104" font-size="8" letter-spacing="12">SUITES</text>

      <g class="contact-row">
        <text class="contact-text" x="465" y="127" text-anchor="end">907 -581-6142</text>
        <circle cx="488" cy="123" r="12.5" fill="var(--ink-white)"/>
        <path d="M483.5 116.5c1.5-.8 2.6.6 3 1.8.3 1-.6 1.6-1 2.2.6 1.6 1.8 3 3.3 3.8.6-.4 1.3-1.3 2.3-.9 1.1.5 2.4 1.6 1.6 3-1.2 2-4 1.6-6.2-.2-2.5-2-4.4-5.2-4.3-7.4 0-1 .5-1.8 1.3-2.3z" fill="var(--card-black)"/>
      </g>
      <g class="contact-row">
        <text class="contact-text" x="465" y="173" text-anchor="end">marrowby_suites@mailnest.net</text>
        <circle cx="488" cy="169" r="12.5" fill="var(--ink-white)"/>
        <rect x="481" y="164" width="14" height="10" fill="none" stroke="var(--card-black)" stroke-width="1.5"/>
        <polyline points="481,164 488,170 495,164" fill="none" stroke="var(--card-black)" stroke-width="1.5"/>
      </g>
      <g class="contact-row">
        <text class="contact-text" x="465" y="219" text-anchor="end">Brantwell Avenue kestrelport Alaska 99571</text>
        <circle cx="488" cy="215" r="12.5" fill="var(--ink-white)"/>
        <path d="M481 216l7-7 7 7h-2v6h-3.5v-4h-3v4H483v-6z" fill="var(--card-black)"/>
      </g>

      <line class="dash" x1="404" y1="299" x2="428" y2="299" stroke="var(--navy)" stroke-width="0.8"/>
      <text class="mini-name" x="466" y="302" text-anchor="middle">MARROWBY</text>
      <line class="dash" x1="504" y1="299" x2="516" y2="299" stroke="var(--navy)" stroke-width="0.8"/>
    </svg>
  </section>

</main>
</body>
</html>
```